Flyer-Design für Kindertagesstätte
Zielgruppe
Wir sind eine Kindertagesstätte und wollen eine Baby-Kind-Spielgruppe jeden Mittwoch in unserer Kita von 09.00 Uhr bis 11.00 Uhr anbieten.
Aufgabenstellung
Unser LOGO muss im Flyer enthalten sein, auf jeden Fall ein Bild wenn möglich mit mehreren Babys/Kleinkindern bis 1,5 Jahre. Wir benötigen den Flyer in DIN lang - bunt - 1 seitig.
Folgender Text sollte enthalten: Baby-Kind-Spielgruppe, jeden mittwoch in unserer Kita 'Fellmuths Spielgarten' von 09.00 Uhr bis 11.00 Uhr. Die Spielgruppe wird durch unser ausgebildetes Fachpersonal begleitet.

```html
<!DOCTYPE html>
<html lang="de">
<head>
<meta charset="utf-8">
<title>Spielgruppe Baby-Kind – Flyer</title>
<link rel="stylesheet" href="https://fonts.googleapis.com/css2?family=Arimo:wght@400;700&display=swap">
<style>
  :root {
    --page-bg: #d4d4d4;
    --red-deep: #a22329;
    --red-bright: #c9263c;
    --red-pink: #d3304c;
    --yellow-top: #dfae3e;
    --yellow-bottom: #ecca5c;
    --text-red: #a8202c;
    --white: #ffffff;
    --photo-light: #e9e7e5;
    --photo-warm: #efe4d8;
    --logo-bg: #eeeeee;
    --logo-ink: #5a2a1e;
  }
  html, body {
    margin: 0;
    width: 1200px;
    height: 800px;
    overflow: hidden;
    background: var(--page-bg);
  }
  .flyer {
    position: absolute;
    left: 50px;
    top: 141px;
    width: 1100px;
    height: 518px;
    box-shadow: 0 18px 40px rgba(0,0,0,0.25);
  }
  .flyer svg { display: block; }
  .flyer-text {
    font-family: "Arimo", Arial, sans-serif;
    fill: var(--text-red);
  }
  .headline {
    font-family: "Arimo", Arial, sans-serif;
    font-weight: 700;
    font-size: 58px;
    letter-spacing: 3px;
    fill: var(--white);
  }
  .info-small { font-size: 20px; }
  .info-strong { font-size: 28px; font-weight: 700; letter-spacing: 1px; }
  .info-time { font-size: 24px; font-weight: 700; letter-spacing: 1px; }
  .info-body { font-size: 21px; }
  .logo-name {
    font-family: "Arimo", Arial, sans-serif;
    font-weight: 700;
    font-size: 15px;
    fill: var(--logo-ink);
  }
  .divider { stroke: var(--white); stroke-width: 3; fill: none; }
</style>
</head>
<body>
<div class="flyer">
  <svg width="1100" height="518" viewBox="0 0 1100 518" xmlns="http://www.w3.org/2000/svg">
    <defs>
      <linearGradient id="yellowFill" x1="0" y1="0" x2="0" y2="1">
        <stop offset="0" stop-color="var(--yellow-top)"/>
        <stop offset="1" stop-color="var(--yellow-bottom)"/>
      </linearGradient>
      <linearGradient id="redRight" x1="0" y1="0" x2="1" y2="1">
        <stop offset="0" stop-color="var(--red-bright)"/>
        <stop offset="1" stop-color="var(--red-pink)"/>
      </linearGradient>
      <linearGradient id="photoBaby" x1="0" y1="0" x2="1" y2="1">
        <stop offset="0" stop-color="#f1efed"/>
        <stop offset="0.5" stop-color="#e6dfd8"/>
        <stop offset="1" stop-color="#dcd8d4"/>
      </linearGradient>
      <linearGradient id="photoPlay" x1="0" y1="0" x2="1" y2="1">
        <stop offset="0" stop-color="#f4ede6"/>
        <stop offset="1" stop-color="#e2d3c4"/>
      </linearGradient>
    </defs>

    <!-- photo area: laughing baby with building blocks -->
    <polygon class="photo-baby" role="img" aria-label="Foto: lachendes Baby mit bunter Mütze zwischen Bausteinen"
             points="0,0 470,0 240,290 150,360 0,360" fill="url(#photoBaby)"/>

    <!-- lower-left red wedge -->
    <polygon class="panel-red-left" points="150,360 240,290 520,518 150,518" fill="var(--red-deep)"/>

    <!-- right red panel -->
    <polygon class="panel-red-right" points="640,0 1100,0 1100,460 860,330" fill="url(#redRight)"/>

    <!-- photo area: educator and toddler playing -->
    <polygon class="photo-play" role="img" aria-label="Foto: Erzieherin und Kleinkind klatschen sich beim Spielen ab"
             points="860,330 1100,460 1100,518 640,518" fill="url(#photoPlay)"/>

    <!-- central yellow diamond -->
    <polygon class="panel-yellow" points="470,0 640,0 860,330 640,518 520,518 240,290" fill="url(#yellowFill)"/>

    <!-- white dividers -->
    <polyline class="divider" points="470,0 240,290 520,518"/>
    <polyline class="divider" points="640,0 860,330 640,518"/>
    <polyline class="divider" points="240,290 150,360"/>
    <polyline class="divider" points="860,330 1100,460"/>

    <!-- logo field -->
    <rect class="logo-box" x="0" y="360" width="150" height="158" fill="var(--logo-bg)"/>
    <circle cx="75" cy="410" r="22" fill="var(--red-deep)"/>
    <text class="logo-name" x="75" y="462" text-anchor="middle">Fellmuths</text>
    <text class="logo-name" x="75" y="481" text-anchor="middle">Spielgarten</text>

    <!-- headline -->
    <text class="headline" x="1070" y="92" text-anchor="end">Spielgruppe</text>
    <text class="headline" x="1070" y="160" text-anchor="end">Baby-Kind</text>

    <!-- info text -->
    <g class="flyer-text" text-anchor="middle">
      <text class="info-small" x="555" y="150">jeden Mittwoch in unserer Kita</text>
      <text class="info-strong" x="555" y="200">„Fellmuths Spielgarten“</text>
      <text class="info-small" x="555" y="232">von</text>
      <text class="info-time" x="555" y="266">09.00 Uhr bis 11.00 Uhr</text>
      <text class="info-body" x="555" y="318">Die Spielgruppe wird durch unser</text>
      <text class="info-body" x="555" y="346">ausgebildetes Fachpersonal</text>
      <text class="info-body" x="555" y="374">begleitet.</text>
    </g>
  </svg>
</div>
</body>
</html>
```